InfoGraphic for Security Pyramid

I've created an infographic that I would like to be redone more professionally. you can see the page in this powerpoint called the pyramid of security. What I'd like done is to replace the background graphic with a new icon in a cartoony format like the one behind end point protection as an example (thats a stock photo).

Target Market(s)

Business Owners

Font styles to use
Sans Serif

Colors
ec1f27
0355a3
f37122

Requirements
Must have
• Consistent images, text must be editable.

```html
<!DOCTYPE html>
<html lang="en">
<head>
<meta charset="utf-8">
<title>Pyramid of Security – Trivela Systems</title>
<link rel="stylesheet" href="https://fonts.googleapis.com/css2?family=Open+Sans:wght@600;700;800&display=swap">
<style>
  :root {
    --navy: #0b0f2e;
    --blue: #0b6fb8;
    --blue-deep: #0355a3;
    --blue-fold: #0a4a85;
    --orange: #f37122;
    --red: #ec1f27;
    --green: #1e9a49;
    --grey: #c3c4c6;
    --white: #ffffff;
  }
  * { box-sizing: border-box; margin: 0; padding: 0; }
  html, body { width: 1200px; height: 2230px; overflow: hidden; background: var(--white); }
  body { font-family: "Open Sans", Arial, sans-serif; position: relative; }

  .hero { position: absolute; left: 0; top: 0; width: 1200px; height: 1063px; background: var(--navy); }
  .brand { position: absolute; font-weight: 800; letter-spacing: 0.5px; display: flex; align-items: center; gap: 12px; }
  .brand-mark { width: 26px; height: 26px; border-radius: 50%; background: var(--orange); }
  .brand--top { left: 78px; top: 52px; font-size: 44px; color: var(--orange); }
  .brand--foot { right: 34px; bottom: 102px; font-size: 44px; color: var(--blue-deep); }

  .title-ribbon { position: absolute; left: 0; top: 164px; width: 1200px; height: 145px; }
  .title { position: absolute; left: 52px; top: 164px; width: 1096px; height: 104px;
    display: flex; align-items: center; justify-content: center;
    color: var(--white); font-weight: 800; font-size: 68px; letter-spacing: 1px; }

  .pyramid { position: absolute; left: 0; top: 0; width: 1200px; height: 1063px; }
  .cell-label { font-family: "Open Sans", Arial, sans-serif; font-weight: 700; font-size: 8.6px; fill: var(--white); text-anchor: middle; }
  .icon { fill: none; stroke: var(--white); stroke-width: 2.6; stroke-linecap: round; stroke-linejoin: round; }
  .icon-fill { fill: var(--white); }

  .diamond { position: absolute; left: 0; top: 1063px; width: 1200px; height: 1167px; }

  .service { position: absolute; width: 324px; height: 314px; border-radius: 27px; padding: 52px 0 0 34px; color: var(--white); }
  .service--orange { background: var(--orange); }
  .service--blue { background: var(--blue); }
  .service h2 { font-size: 24px; font-weight: 700; margin-bottom: 22px; }
  .service ul { list-style: none; font-weight: 700; font-size: 20px; line-height: 27px; }
  .service li::before { content: "•"; }

  .footer-band { position: absolute; left: 0; bottom: 0; width: 1200px; height: 76px; }
  .footer-contact { position: absolute; left: 78px; bottom: 16px; color: var(--white); font-weight: 700; font-size: 33px; letter-spacing: 3px; }
</style>
</head>
<body>

<section class="hero">
  <div class="brand brand--top"><span class="brand-mark"></span>Trivela Systems</div>

  <svg class="title-ribbon" viewBox="0 110 807 97.5" preserveAspectRatio="none" aria-hidden="true">
    <polygon points="0,135 35,135 35,180 95,205 0,205" fill="var(--blue-fold)"/>
    <polygon points="807,135 772,135 772,180 712,205 807,205" fill="var(--blue-fold)"/>
    <polygon points="35,180 95,180 95,205" fill="#06325d"/>
    <polygon points="772,180 712,180 712,205" fill="#06325d"/>
    <rect x="35" y="110" width="737" height="70" fill="var(--blue)"/>
  </svg>
  <h1 class="title">PYRAMID OF SECURITY</h1>

  <svg class="pyramid" viewBox="0 0 807 715" aria-label="Pyramid of security layers">
    <polygon points="404,213 83,667 724,667" fill="var(--white)"/>

    <!-- row 1 -->
    <polygon points="404,222 468,313 340,313" fill="var(--orange)"/>
    <rect x="394" y="262" width="18" height="24" fill="#ffffff" opacity="0.9" role="img" aria-label="Icon of a person climbing steps"/>
    <text class="cell-label" x="404" y="307">USER TRAINING</text>

    <!-- row 2 -->
    <polygon points="337,317 402,317 402,398 280,398" fill="var(--blue)"/>
    <g class="icon"><path d="M348,340 a6,6 0 0 1 10,-6 a6,6 0 0 1 11,4 h-21z"/><path d="M352,346v6M358,346v6M364,346v6"/></g>
    <rect x="345" y="358" width="24" height="12" class="icon-fill"/>
    <text class="cell-label" x="358" y="391">WEB FILTERING</text>
    <polygon points="406,317 471,317 528,398 406,398" fill="var(--green)"/>
    <g class="icon"><circle cx="442" cy="344" r="18"/><circle cx="442" cy="344" r="11"/><circle cx="442" cy="344" r="4"/><path d="M442,344l12,-10"/></g>
    <text class="cell-label" x="458" y="380">CONTINUOUS</text>
    <text class="cell-label" x="458" y="391">SCANNING</text>

    <!-- row 3 -->
    <polygon points="277,402 341,402 341,485 219,485" fill="var(--red)"/>
    <rect x="280" y="412" width="40" height="36" rx="14" fill="#ffffff" opacity="0.85" role="img" aria-label="Icon of a brain with circuit lines"/>
    <text class="cell-label" x="295" y="478">THREAT INTEL</text>
    <polygon points="345,402 461,402 461,485 345,485" fill="var(--orange)"/>
    <g class="icon-fill"><rect x="366" y="442" width="12" height="28"/><rect x="384" y="432" width="12" height="38"/><rect x="402" y="446" width="12" height="24"/><rect x="420" y="424" width="12" height="46"/></g>
    <path class="icon" d="M372,430 l18,-14 l14,10 l24,-20"/>
    <text class="cell-label" x="403" y="478">ASSET MANAGEMENT</text>
    <polygon points="465,402 531,402 589,485 465,485" fill="var(--blue)"/>
    <g class="icon"><circle cx="507" cy="436" r="19"/><circle cx="503" cy="431" r="5"/><path d="M494,446 a9,7 0 0 1 15,-4"/><circle cx="512" cy="444" r="4"/></g>
    <text class="cell-label" x="526" y="478">MINIMIZE ADMIN</text>

    <!-- row 4 -->
    <polygon points="216,489 282,489 282,570 159,570" fill="var(--green)"/>
    <rect x="220" y="500" width="46" height="46" fill="none" stroke="#ffffff" stroke-width="2"/>
    <text x="224" y="511" font-size="8.6" font-weight="700" fill="#fff" font-family="Open Sans, sans-serif">10011010</text>
    <text x="224" y="521" font-size="8.6" font-weight="700" fill="#fff" font-family="Open Sans, sans-serif">01011100</text>
    <text x="224" y="531" font-size="8.6" font-weight="700" fill="#fff" font-family="Open Sans, sans-serif">10101001</text>
    <text x="224" y="541" font-size="8.6" font-weight="700" fill="#fff" font-family="Open Sans, sans-serif">01010110</text>
    <rect x="203" y="539" width="12" height="7" fill="none" stroke="#fff" stroke-width="2"/>
    <text class="cell-label" x="215" y="564">NEXT GEN FIREWALL</text>
    <polygon points="286,489 401,489 401,570 286,570" fill="var(--red)"/>
    <rect x="326" y="496" width="24" height="44" rx="4" class="icon"/>
    <circle cx="356" cy="526" r="11" fill="var(--red)" stroke="#fff" stroke-width="2.6"/>
    <path d="M356,519 l6,3 v4 c0,4 -3,6 -6,7 c-3,-1 -6,-3 -6,-7 v-4z" class="icon-fill"/>
    <text class="cell-label" x="343" y="564">MOBILE SECURITY</text>
    <polygon points="405,489 520,489 520,570 405,570" fill="var(--blue)"/>
    <g class="icon" stroke-width="1.8"><rect x="447" y="498" width="26" height="12"/><path d="M460,510v8h-24M436,518v14M460,518h20v14"/><path d="M428,524l8,-6 8,6 -8,6z"/><rect x="473" y="532" width="26" height="12"/><path d="M455,534l6,-5 6,5 -6,5z"/></g>
    <text class="cell-label" x="462" y="564">SOPS</text>
    <polygon points="524,489 592,489 649,570 524,570" fill="var(--green)"/>
    <g class="icon"><path d="M560,500h22v46h-22"/><path d="M570,502l12,-2v46l-12,-4z" class="icon-fill"/><path d="M540,523h16M550,517l6,6 -6,6"/></g>
    <text class="cell-label" x="580" y="564">LOGGING</text>

    <!-- row 5 -->
    <polygon points="156,574 222,574 222,660 95,660" fill="var(--orange)"/>
    <g class="icon-fill"><circle cx="172" cy="598" r="1.6"/><circle cx="177" cy="601" r="1.6"/><circle cx="177" cy="607" r="1.6"/><circle cx="172" cy="610" r="1.6"/><circle cx="167" cy="607" r="1.6"/><circle cx="167" cy="601" r="1.6"/></g>
    <rect x="136" y="620" width="76" height="6" rx="3" fill="none" stroke="#fff" stroke-width="1.6"/>
    <rect x="136" y="620" width="34" height="6" rx="3" class="icon-fill"/>
    <text class="cell-label" x="156" y="652">UPDATING</text>
    <polygon points="226,574 341,574 341,660 226,660" fill="var(--blue)"/>
    <circle cx="244" cy="620" r="11" class="icon-fill"/><path d="M239,620l4,4 7,-8" stroke="var(--blue)" stroke-width="2.6" fill="none"/>
    <rect x="270" y="606" width="28" height="26" rx="3" class="icon-fill"/><path class="icon" stroke-width="4" d="M276,606v-8a8,8 0 0 1 16,0v8"/>
    <circle cx="284" cy="617" r="3" fill="var(--blue)"/><rect x="283" y="618" width="2.4" height="8" fill="var(--blue)"/>
    <circle cx="324" cy="620" r="11" class="icon-fill"/><path d="M320,616l8,8M328,616l-8,8" stroke="var(--blue)" stroke-width="2.6"/>
    <text class="cell-label" x="284" y="652">PASSWORDS</text>
    <polygon points="345,574 461,574 461,660 345,660" fill="var(--green)"/>
    <path class="icon-fill" d="M382,634 a13,13 0 0 1 4,-25 a17,17 0 0 1 32,-2 a14,14 0 0 1 6,27z"/>
    <path d="M403,628v-16M395,618l8,-8 8,8" stroke="var(--green)" stroke-width="4" fill="none"/>
    <text class="cell-label" x="403" y="652">BACKUPS</text>
    <polygon points="465,574 581,574 581,660 465,660" fill="var(--orange)"/>
    <rect x="491" y="582" width="36" height="36" fill="#ffffff" opacity="0.85" role="img" aria-label="Icon of a computer with protection spray"/>
    <rect x="540" y="592" width="10" height="22" rx="2" fill="#ffffff" opacity="0.85"/>
    <text class="cell-label" x="523" y="641">ENDPOINT</text>
    <text class="cell-label" x="523" y="652">PROTECTION</text>
    <polygon points="585,574 652,574 713,660 585,660" fill="var(--blue)"/>
    <rect x="608" y="594" width="40" height="28" class="icon"/><path class="icon" d="M608,594l20,16 20,-16"/>
    <circle cx="650" cy="626" r="10" fill="var(--blue)" stroke="#fff" stroke-width="2.4"/><rect x="645" y="625" width="10" height="7" class="icon-fill"/><path class="icon" stroke-width="1.8" d="M647,625v-3a3,3 0 0 1 6,0v3"/>
    <text class="cell-label" x="640" y="652">EMAIL SECURITY</text>
  </svg>
</section>

<svg class="diamond" viewBox="0 715 807 785" preserveAspectRatio="none" aria-hidden="true">
  <polygon points="404,730 742,1080 404,1430 68,1080" fill="var(--grey)"/>
  <polygon points="404,750 722,1080 404,1410 88,1080" fill="none" stroke="var(--white)" stroke-width="6"/>
</svg>

<div class="service service--orange" style="left:245px; top:1243px;">
  <h2>CyberSecurity</h2>
  <ul><li>Assessments</li><li>Penetration Tests</li><li>Protection Services</li><li>Compliance Review</li></ul>
</div>
<div class="service service--blue" style="left:630px; top:1243px;">
  <h2>IT Support</h2>
  <ul><li>Remote/Onsite Support</li><li>Project Work</li><li>Automated Management</li><li>Alerting/Reporting</li></ul>
</div>
<div class="service service--blue" style="left:247px; top:1615px;">
  <h2>Virtual CIO</h2>
  <ul><li>Align Tech-Business</li><li>Budgeting</li><li>Tech Roadmap</li><li>Policy Developement</li></ul>
</div>
<div class="service service--orange" style="left:630px; top:1615px;">
  <h2>Services</h2>
  <ul><li>Office Suite</li><li>Phone Services</li><li>Secure Cloud Services</li><li>Secure File Sharing</li></ul>
</div>

<div class="brand brand--foot"><span class="brand-mark"></span>Trivela Systems</div>

<svg class="footer-band" viewBox="0 0 1200 76" preserveAspectRatio="none" aria-hidden="true">
  <polygon points="0,0 772,0 810,76 0,76" fill="var(--blue)"/>
</svg>
<div class="footer-contact">555-014-2290 | trivelasys.com</div>

</body>
</html>
```